Creative Report - A Presentation

We are looking for a report to visual workers' compensation claim data and the impact claims have on premium. I’m looking for something that is very visually new, appealing, easy to understand, and cutting edge.

Right now we are looking for 6 pages to be designed: a cover page, an informative page, and 4 reports. The key data for the last 3 reports are listed in the other document attached named “Key Data for Report”. These should be designed in a 8.5 x 11 page layout.

I would prefer a way where things can be combined without looking too crowded. You can play around with the background, for printing purposes try to leave white space.

Attached are a few graphs that I found that I like the look of. Please design when YOU think is best. The docx & the comments on the side are just to help you visualize.

We are a mod analysis company that is always developing new reports. We are hoping to find a designer we can work with in the future as well – think of this as a trial run!

2 designers reached out this morning wanting to submit designs, I would like to see what they have.

```html
<!DOCTYPE html>
<html lang="en">
<head>
<meta charset="utf-8">
<title>Workers Compensation Executive Summary</title>
<link href="https://fonts.googleapis.com/css2?family=Poppins:wght@300;400;500;600;700;800&family=Oswald:wght@400;500;600&display=swap" rel="stylesheet">
<style>
:root{
  --bg:#dcdcdc;
  --paper:#ffffff;
  --blue:#0bb0ef;
  --blue-dark:#0a78b5;
  --navy:#0f2a3d;
  --ink:#1e2226;
  --muted:#55606a;
  --stripe:#eef0f2;
  --red:#c8102e;
}
*{box-sizing:border-box;margin:0;padding:0}
html,body{width:1200px;height:2177px;overflow:hidden}
body{background:var(--bg);font-family:"Poppins",sans-serif;color:var(--ink);position:relative}
.page{position:absolute;width:487px;height:630px;background:var(--paper);box-shadow:0 6px 18px rgba(0,0,0,.18);overflow:hidden}
.abs{position:absolute}
.p-cover{left:88px;top:102px}
.p-intro{left:625px;top:102px}
.p-mod{left:88px;top:769px}
.p-medical{left:625px;top:769px}
.p-cause{left:88px;top:1439px}
.p-nature{left:625px;top:1439px}

.h2{font-weight:700;font-size:12.5px;color:var(--navy);letter-spacing:-.1px}
.h2 span{color:var(--blue)}
.body{font-size:6.8px;line-height:1.38;color:var(--ink)}
.checks{list-style:none}
.checks li{position:relative;padding-left:11px;font-size:6.8px;line-height:1.35;font-weight:500}
.checks li::before{content:"";position:absolute;left:0;top:1.5px;width:6px;height:6px;border:1px solid var(--blue);border-radius:1px}
.checks li::after{content:"";position:absolute;left:1.8px;top:2.5px;width:2px;height:3.5px;border:solid var(--blue);border-width:0 1.2px 1.2px 0;transform:rotate(45deg)}

.disclaimer{position:absolute;left:34px;top:586px;width:275px;font-size:4.5px;line-height:1.3;color:var(--ink);font-weight:500}
.brand{position:absolute;display:flex;align-items:center;gap:4px;font-weight:700;color:var(--navy);font-size:11px;letter-spacing:.3px}
.brand i{display:block;width:12px;height:12px;border-radius:50%;background:var(--blue)}
.pg{position:absolute;left:425px;top:582px;width:28px;height:48px;background:var(--navy);color:#fff;font-size:6.5px;text-align:center;padding-top:9px}
.faint-photo{position:absolute;left:0;width:100%;background:linear-gradient(180deg,rgba(255,255,255,1) 0%,rgba(228,234,238,.55) 45%,rgba(255,255,255,1) 100%)}

/* cover */
.cover-photo{position:absolute;left:0;top:0;width:487px;height:490px;background:linear-gradient(160deg,#5b6670 0%,#2e3b47 35%,#1f4f78 70%,#1a6da6 100%)}
.cover-title{position:absolute;left:37px;top:390px;color:#fff;font-weight:800;font-size:34px;line-height:1.06;letter-spacing:.2px}
.cover-band{position:absolute;left:0;top:472px;width:336px;height:32px;background:var(--blue);color:#fff;font-weight:400;font-size:16px;letter-spacing:5px;padding:6px 0 0 37px}
.mod-eff{position:absolute;left:37px;top:522px;font-family:"Oswald",sans-serif;font-size:14px;letter-spacing:1.6px;color:var(--navy);font-weight:400}
.mod-eff b{font-weight:600}
.contact{position:absolute;left:37px;top:546px;font-size:6.6px;line-height:1.65}
.contact .name{color:var(--blue);font-weight:700;font-size:8px}
.contact svg{vertical-align:-1px;margin-right:2px}

/* intro */
.feature{position:absolute;top:396px;width:116px;text-align:center}
.feature svg{display:block;margin:0 auto 8px}
.feature p{font-size:7px;line-height:1.3;color:var(--ink)}
.divider{position:absolute;top:396px;width:1px;height:150px;background:#e3e7ea}

/* mod */
.track{position:absolute;left:37px;top:104px;width:405px;height:25px;border-radius:13px;background:#e6e8ea}
.fill{position:absolute;left:77px;top:104px;width:270px;height:25px;border-radius:13px;background:var(--blue)}
.tick{position:absolute;top:97px;width:1px;height:40px;background:#9aa3ab}
.marker{position:absolute;top:141px;width:34px;height:34px;border-radius:50%;background:var(--navy);color:var(--blue);text-align:center;font-family:"Oswald",sans-serif;font-weight:600;font-size:10px;line-height:1;padding-top:9px}
.marker small{display:block;font-family:"Poppins",sans-serif;color:#fff;font-size:3.6px;font-weight:400;margin-top:1px}
.marker::before{content:"";position:absolute;left:13px;top:-6px;border:4px solid transparent;border-bottom:4px solid var(--navy);border-left-width:4px}
.accent{position:absolute;left:0;top:215px;width:3px;height:90px;background:var(--blue)}

/* medical */
.row-band{position:absolute;left:0;width:230px;height:20px;background:#f0f2f4;font-size:7.2px;padding:5px 0 0 38px}
.pill{position:absolute;left:234px;width:97px;height:23px;border-radius:12px;background:var(--blue);color:#fff;font-family:"Oswald",sans-serif;font-size:15px;padding:1px 0 0 18px;white-space:nowrap}
.pill sup{font-size:7px;vertical-align:7px}
.pill small{font-family:"Poppins",sans-serif;font-size:4.6px;display:inline-block;line-height:1;vertical-align:2px}
.chart-label{position:absolute;font-size:6.2px;line-height:1.3}
.chart-label b{font-weight:700;font-size:7px;color:var(--navy);display:block}

.data{position:absolute;border-collapse:collapse;font-size:5.6px;border-radius:6px;overflow:hidden}
.data th{background:var(--navy);color:#fff;font-weight:600;font-size:6.6px;height:30px;padding:0 4px;line-height:1.1}
.data td{height:18.5px;padding:0 6px;text-align:center;border-right:1px solid #fff}
.data td:first-child{text-align:left}
.data tbody tr:nth-child(odd) td{background:#f3f4f5}
.data tbody tr:nth-child(even) td{background:#e6e8ea}

/* cause pie labels */
.pie-lab{position:absolute;text-align:center;font-size:5.6px;line-height:1.1;transform:translateX(-50%);width:70px}
.pie-lab b{display:block;font-family:"Oswald",sans-serif;font-weight:500;font-size:13px;color:var(--navy)}
.pie-lab.light b{color:var(--blue)}

/* nature cards */
.card{position:absolute;width:230px;height:62px}
.card .icon{position:absolute;left:0;top:0;width:28px;height:28px;border-radius:50%;border:2px solid var(--blue);background:#fff}
.card .icon::after{content:"";position:absolute;left:6px;top:6px;width:12px;height:12px;border-radius:50%;background:var(--navy)}
.card .lbl{position:absolute;left:-4px;top:31px;width:48px;font-size:5.4px;font-weight:600;line-height:1.15}
.card .grid{position:absolute;left:42px;top:-2px;width:145px}
.card .r{display:flex;height:11px;align-items:center;margin-bottom:.5px}
.card .r span{flex:1;font-size:5.4px;padding-left:9px;background:var(--stripe);height:100%;line-height:11px}
.card .r em{font-style:normal;width:59px;height:9px;border-radius:5px;background:var(--navy);color:#fff;font-size:5.4px;text-align:center;line-height:9px;margin-left:2px;font-weight:600}
.card .r.last span{background:#dff3fc;font-weight:700}
.card .r.last em{background:var(--red)}
</style>
</head>
<body>

<!-- COVER -->
<section class="page p-cover">
  <div class="cover-photo" role="img" aria-label="Photo of two business people shaking hands over a desk with banknotes"></div>
  <h1 class="cover-title">WORKERS<br>COMPENSATION</h1>
  <div class="cover-band">EXECUTIVE SUMMARY</div>
  <div class="mod-eff">MOD EFFECTIVE <b>10-08-2022</b></div>
  <div class="contact">
    <div class="name">MARCUS HALE</div>
    <div><svg width="7" height="7" viewBox="0 0 10 10"><path d="M2 1l2 2-1 1.5a6 6 0 0 0 2.5 2.5L7 6l2 2-1.5 1.5C4 9 1 6 .5 2z" fill="none" stroke="#0bb0ef" stroke-width="1"/></svg>(555) 0142 7788</div>
    <div><svg width="7" height="7" viewBox="0 0 10 10"><rect x=".5" y="2" width="9" height="6" fill="none" stroke="#0bb0ef"/><path d="M.5 2l4.5 3.5L9.5 2" fill="none" stroke="#0bb0ef"/></svg>info@claimwise-reports.com</div>
  </div>
  <div class="brand" style="left:335px;top:556px;font-size:15px"><i style="width:18px;height:18px"></i>CLAIMWISE</div>
  <p class="disclaimer" style="left:37px;top:593px;width:420px">Proprietary and Confidential. Ratewell Inc. provides for an ESTIMATE of an experience modification factor. Your official experience modification factor is issued solely by the applicable workers' compensation rating bureau. Ratewell Inc. All Rights Reserved.</p>
</section>

<!-- INTRO -->
<section class="page p-intro">
  <div class="faint-photo" style="top:380px;height:190px" role="img" aria-label="Faint background photo of an office desk"></div>
  <p class="body abs" style="left:38px;top:44px;width:415px">Workers compensation claims can have a significant impact on a business. In addition to the direct claim costs, there are many other costs associated with a workers compensation claim that can impact a business</p>
  <div class="abs" style="left:38px;top:83px;font-size:12.5px;font-weight:600;color:var(--blue)">They are</div>
  <ul class="checks abs" style="left:38px;top:104px;width:300px;line-height:2.2">
    <li style="margin-bottom:5.3px">Work Comp Premium Costs</li>
    <li style="margin-bottom:5.3px">Overtime</li>
    <li style="margin-bottom:5.3px">Administrative time spent on claim after an injury</li>
    <li style="margin-bottom:5.3px">Lost Opportunities due to staffing</li>
    <li style="margin-bottom:5.3px">Lost Productivity</li>
    <li>Clean up or repair of damaged equipment</li>
  </ul>
  <h2 class="h2 abs" style="left:38px;top:224px;width:420px;line-height:1.28;font-size:13px">OSHA estimates that depending upon the size of the claim indirect costs range from <span>1 to 4 times the direct costs</span></h2>
  <p class="body abs" style="left:38px;top:263px;width:405px">The following report explains in detail how a workers compensation claim affects the premium that your business pays for workers compensation. Most business have an experience mod that is reflective of their past claims experience and every claim has an impact on the experience mod. It is important to note that some claims affect the mod differently.</p>
  <ul class="checks abs" style="left:38px;top:311px;width:410px">
    <li style="margin-bottom:7px">A medical only claim is reduced by 70% in the mod calculation.</li>
    <li style="margin-bottom:7px">A medical/indemnity claim has no reduction.</li>
    <li>All claims are also limited by a primary threshold value where claims are grouped into primary claims and excess claims.</li>
  </ul>
  <div class="feature" style="left:38px">
    <svg width="34" height="36" viewBox="0 0 34 36" fill="none" stroke="#0bb0ef" stroke-width="1.3"><rect x="2" y="2" width="30" height="32" rx="2"/><path d="M2 8h30"/><path d="M7 26l6-7 5 4 8-10"/><path d="M8 32v-3M13 32v-6M18 32v-4M23 32v-8"/></svg>
    <p>The following report will analyze the types of claims that are occurring in your business and will group them together for ease of identifying trends and areas of opportunity to improve.</p>
  </div>
  <div class="divider" style="left:170px"></div>
  <div class="feature" style="left:185px">
    <svg width="40" height="36" viewBox="0 0 40 36" fill="none" stroke="#0bb0ef" stroke-width="1.3"><circle cx="20" cy="10" r="6"/><circle cx="20" cy="10" r="2.2"/><rect x="6" y="20" width="12" height="12" rx="1"/><path d="M9 24h6M9 28h6"/><rect x="24" y="20" width="12" height="12" rx="1"/><path d="M27 24h6M27 28h6"/><path d="M20 16v4"/></svg>
    <p>By identifying the types and causes of losses many times a cost/benefit analysis can be performed to allow for safety training, additional equipment or building or process improvements.</p>
  </div>
  <div class="divider" style="left:316px"></div>
  <div class="feature" style="left:330px">
    <svg width="38" height="36" viewBox="0 0 38 36" fill="none" stroke="#0bb0ef" stroke-width="1.3"><rect x="10" y="2" width="22" height="32" rx="2"/><rect x="14" y="6" width="14" height="7"/><path d="M15 18h3M21 18h3M27 18h1M15 23h3M21 23h3M15 28h3M21 28h3"/><circle cx="8" cy="27" r="6"/><path d="M8 24v6M6 25.5h3.5M6 28.5h3.5"/></svg>
    <p>For the premium cost analysis in this report we have used a manual premium of $XXX,XXX. A manual premium is the premium derived by the carrier before any credits, debits, or experience rating.</p>
  </div>
  <p class="disclaimer">Proprietary and Confidential. Ratewell Inc. provides for an ESTIMATE of an experience modification factor. Your official experience modification factor is issued solely by the applicable workers' compensation rating bureau. Ratewell Inc. All Rights Reserved.</p>
  <div class="brand" style="left:335px;top:592px"><i></i>CLAIMWISE</div>
  <div class="pg">Pg 1</div>
</section>

<!-- EXPERIENCE MOD -->
<section class="page p-mod">
  <div class="faint-photo" style="top:400px;height:180px" role="img" aria-label="Faint background photo of a person at a desk"></div>
  <h2 class="h2 abs" style="left:38px;top:40px">YOUR EXPERIENCE <span>MOD</span></h2>
  <p class="body abs" style="left:38px;top:60px">The report below shows your company's actual experience mod as well as your lowest possible mod.</p>
  <div class="tick" style="left:37px"></div>
  <div class="tick" style="left:441px"></div>
  <div class="track"></div>
  <div class="fill"></div>
  <div class="tick" style="left:77px;top:100px;height:45px"></div>
  <div class="tick" style="left:346px;top:100px;height:45px"></div>
  <div class="marker" style="left:60px">0.63<small>Min Mod</small></div>
  <div class="marker" style="left:329px">1.19<small>Actual Mod</small></div>
  <div class="accent"></div>
  <h2 class="h2 abs" style="left:38px;top:212px">MOD VALUE <span>EXPLANATION</span></h2>
  <ul class="checks abs" style="left:38px;top:234px;width:410px">
    <li style="margin-bottom:12px">A mod value below 1.0 means your company is performing better than your peers. If your company had no claims your lowest possible mod value would be 0.632</li>
    <li style="margin-bottom:12px">A mod of 1.0 is considered average</li>
    <li>A mod value above 1.0 means your company is performing worse than your peers and you will pay more in workers compensation premium.</li>
  </ul>
  <h2 class="h2 abs" style="left:38px;top:349px">SUMMARY</h2>
  <p class="body abs" style="left:38px;top:370px;width:405px">The incurred claims reported have a claim impact of .56 on your mod value. This is increasing your premium annually by <b>$112,000.</b></p>
  <p class="body abs" style="left:38px;top:399px;width:405px">In the following pages we'll dig into the types of claims your business is having and look for areas of opportunity to reduce or eliminate claims and lower your mod value.</p>
  <p class="disclaimer">Proprietary and Confidential. Ratewell Inc. provides for an ESTIMATE of an experience modification factor. Your official experience modification factor is issued solely by the applicable workers' compensation rating bureau. Ratewell Inc. All Rights Reserved.</p>
  <div class="brand" style="left:335px;top:592px"><i></i>CLAIMWISE</div>
  <div class="pg">Pg 2</div>
</section>

<!-- MEDICAL VS INDEMNITY -->
<section class="page p-medical">
  <div class="faint-photo" style="top:290px;height:170px" role="img" aria-label="Faint background photo of a workplace"></div>
  <h2 class="h2 abs" style="left:38px;top:40px">MEDICAL VS MEDICAL/<span>INDEMNITY CLAIMS</span></h2>
  <p class="body abs" style="left:38px;top:64px;width:410px">The type of claims your business is having can have a significant impact on your mod value as not all claims are valued equally. Medical only claims have their value reduced by 70% in the mod calculation and any claim with an indemnity payment is not reduced. This is one of the reasons an effective return to work program can help reduce your premium costs.</p>
  <div class="abs" style="left:38px;top:139px;font-size:7px;font-weight:700">Here's your company's breakdown.</div>
  <div class="row-band" style="top:162px">The total losses for the period reviewed are</div>
  <div class="pill" style="top:160px"><sup>$</sup>284,623</div>
  <div class="row-band" style="top:193px">Medical only claims accounted for</div>
  <div class="pill" style="top:191px"><sup>$</sup>85,719 <small>in<br>losses</small></div>
  <div class="row-band" style="top:223px">Medical/Indemnity claims accounts for</div>
  <div class="pill" style="top:221px"><sup>$</sup>198,904 <small>in<br>losses</small></div>
  <div class="abs" style="left:0;width:487px;top:276px;text-align:center;font-size:12px;color:var(--navy)">MEDICAL VS MEDICAL/INDEMNITY CLAIMS</div>
  <svg class="abs" style="left:176px;top:302px" width="140" height="140" viewBox="-70 -70 140 140" role="img" aria-label="Donut chart of 22 claims split by loss type">
    <circle r="48" fill="none" stroke="#e6f5fc" stroke-width="40"/>
    <path d="M0 0L0 -68A68 68 0 1 0 64.7 21Z" fill="#0bb0ef"/>
    <circle r="28" fill="#fff"/>
    <text x="0" y="6" text-anchor="middle" font-family="Oswald,sans-serif" font-size="25" fill="#0f2a3d">22</text>
    <text x="0" y="15" text-anchor="middle" font-family="Poppins,sans-serif" font-size="5.5" font-weight="600" fill="#0bb0ef">CLAIMS</text>
  </svg>
  <svg class="abs" style="left:155px;top:320px" width="30" height="22" viewBox="0 0 30 22" fill="none" stroke="#0bb0ef" stroke-width="1.4"><path d="M2 4c12-3 20 2 24 14"/><path d="M21 15l5 4 2-6"/></svg>
  <svg class="abs" style="left:298px;top:320px" width="26" height="22" viewBox="0 0 26 22" fill="none" stroke="#0bb0ef" stroke-width="1.4"><path d="M24 3C13 4 6 10 5 18"/><path d="M1 14l4 5 4-4"/></svg>
  <div class="chart-label" style="left:57px;top:316px;width:100px"><b>MEDICAL/INDEMNITY CLAIMS</b>$198,904 incurred losses<br>0.446 mod impact<br>$267,600 3 yr premium impact</div>
  <div class="chart-label" style="left:323px;top:316px;width:100px"><b>MEDICAL ONLY CLAIMS</b>$85,719 incurred losses<br>0.127 mod impact<br>$76,200 3 yr premium impact</div>
  <table class="data" style="left:35px;top:473px;width:420px">
    <thead><tr><th>Loss Type</th><th>Loss Amount</th><th>Mod Impact</th><th>3 year premium<br>Impact</th><th># of Claims</th></tr></thead>
    <tbody>
      <tr><td>Medical Only</td><td>$85,719</td><td>0.127</td><td>$76,200</td><td>15</td></tr>
      <tr><td>Medical/Indemnity</td><td>$198,904</td><td>0.446</td><td>$267,600</td><td>7</td></tr>
      <tr><td></td><td>$284,623</td><td></td><td></td><td></td></tr>
    </tbody>
  </table>
  <p class="disclaimer">Proprietary and Confidential. Ratewell Inc. provides for an ESTIMATE of an experience modification factor. Your official experience modification factor is issued solely by the applicable workers' compensation rating bureau. Ratewell Inc. All Rights Reserved.</p>
  <div class="brand" style="left:335px;top:592px"><i></i>CLAIMWISE</div>
  <div class="pg">Pg 3</div>
</section>

<!-- CLAIMS BY CAUSE -->
<section class="page p-cause">
  <h2 class="h2 abs" style="left:38px;top:40px">CLAIMS BY CAUSE <span>OF INJURY</span></h2>
  <p class="body abs" style="left:38px;top:64px;width:405px">Visually grouping the claims together can help with identifying trends and areas to focus on for improvement and future risk management. The following groupings identify the top losses incurred by your company</p>
  <svg class="abs" style="left:147px;top:134px" width="200" height="200" viewBox="-100 -100 200 200" role="img" aria-label="Pie chart of claim amounts by cause of injury">
    <path d="M0 0L0 -93A93 93 0 0 1 1.9 -93Z" fill="#0f2a3d"/>
    <path d="M0 0L1.9 -93A93 93 0 0 1 89.9 23.8Z" fill="#0a78b5"/>
    <path d="M0 0L89.9 23.8A93 93 0 0 1 -29.2 88.3Z" fill="#075f8e"/>
    <path d="M0 0L-29.2 88.3A93 93 0 0 1 -93 -2.9Z" fill="#0fa9e6"/>
    <path d="M0 0L-93 -2.9A93 93 0 0 1 -63.5 -67.9Z" fill="#0b6fa3"/>
    <path d="M0 0L-63.5 -67.9A93 93 0 0 1 -21.2 -90.5Z" fill="#86d6f6"/>
    <path d="M0 0L-21.2 -90.5A93 93 0 0 1 0 -93Z" fill="#14a4de"/>
    <circle r="34" fill="#fff" opacity=".35"/>
    <circle r="30" fill="#fff"/>
    <text y="-9" text-anchor="middle" font-family="Poppins,sans-serif" font-size="4.4" font-weight="600" fill="#0bb0ef">CLAIMS BY CAUSE OF</text>
    <text y="9" text-anchor="middle" font-family="Oswald,sans-serif" font-size="19" fill="#0bb0ef">INJURY</text>
  </svg>
  <svg class="abs" style="left:0;top:0" width="487" height="330" fill="none" stroke="#1e2226" stroke-width=".6">
    <path d="M182 150v14h10"/><path d="M225 134v12h4"/><path d="M261 128v14"/><path d="M351 172h-10l-9 8"/><path d="M132 186v12h20"/><path d="M139 286v-10h14"/><path d="M327 300v-8h-22"/>
  </svg>
  <div class="pie-lab light" style="left:182px;top:116px"><b>05</b>Motor Vehicle</div>
  <div class="pie-lab light" style="left:225px;top:102px;width:30px"><b>04</b>Burn or Scald</div>
  <div class="pie-lab" style="left:261px;top:96px;width:50px"><b>03</b>Miscellaneous Causes</div>
  <div class="pie-lab light" style="left:355px;top:152px;width:60px"><b>02</b>Fall, slip or trip Injury</div>
  <div class="pie-lab" style="left:132px;top:165px;width:50px"><b>06</b>Strain or injury by</div>
  <div class="pie-lab light" style="left:139px;top:276px;width:55px"><b>07</b>Struck or Injured by</div>
  <div class="pie-lab" style="left:332px;top:310px;width:70px"><b>01</b>Cut, Punture, Scrape Injured by</div>
  <h2 class="h2 abs" style="left:38px;top:358px">CLAIMS BY CAUSE <span>OF INJURY</span></h2>
  <table class="data" style="left:35px;top:382px;width:420px">
    <thead><tr><th>Claim Type</th><th># of Claims</th><th>Claim Amount</th><th>Mod Impact</th><th>3 year Premium<br>Cost</th></tr></thead>
    <tbody>
      <tr><td>Fall, Slip or Trip Injury</td><td>4</td><td>$81,879</td><td>0.137</td><td>$82,200</td></tr>
      <tr><td>Cut, Puncture, Scrape Injured By</td><td>3</td><td>$73,917</td><td>0.130</td><td>$11,400</td></tr>
      <tr><td>Struck or Injured By</td><td>4</td><td>$58,108</td><td>0.087</td><td>$87,600</td></tr>
      <tr><td>Strain or Injury By</td><td>4</td><td>$35,669</td><td>0.146</td><td>$52,200</td></tr>
      <tr><td>Motor Vehicle</td><td>2</td><td>$23,674</td><td>0.032</td><td>$19,200</td></tr>
      <tr><td>Burn or Scald</td><td>4</td><td>$10,426</td><td>0.039</td><td>$23,400</td></tr>
      <tr><td>Miscellaneous Causes</td><td>1</td><td>$950</td><td>0.002</td><td>$1,200</td></tr>
    </tbody>
  </table>
  <p class="disclaimer">Proprietary and Confidential. Ratewell Inc. provides for an ESTIMATE of an experience modification factor. Your official experience modification factor is issued solely by the applicable workers' compensation rating bureau. Ratewell Inc. All Rights Reserved.</p>
  <div class="brand" style="left:335px;top:592px"><i></i>CLAIMWISE</div>
  <div class="pg">Pg 4</div>
</section>

<!-- CLAIMS BY NATURE -->
<section class="page p-nature">
  <div class="faint-photo" style="top:380px;height:190px" role="img" aria-label="Faint background photo of a workplace"></div>
  <h2 class="h2 abs" style="left:36px;top:42px">CLAIMS BY NATURE <span>OF INJURY</span></h2>

  <div class="card" style="left:34px;top:80px"><div class="icon"></div><div class="lbl">All Other Specific Injuries, NOC</div><div class="grid">
    <div class="r"><span># of Claims</span><em>1</em></div><div class="r"><span>Claim Amount</span><em>$18,500</em></div><div class="r"><span>Mod Impact</span><em>0.025</em></div><div class="r last"><span>3 year Premium Cost</span><em>$15,000</em></div></div></div>
  <div class="card" style="left:261px;top:80px"><div class="icon"></div><div class="lbl">Heat Prostration</div><div class="grid" style="left:51px">
    <div class="r"><span># of Claims</span><em>1</em></div><div class="r"><span>Claim Amount</span><em>$950</em></div><div class="r"><span>Mod Impact</span><em>0.002</em></div><div class="r last"><span>3 year Premium Cost</span><em>$1,200</em></div></div></div>

  <div class="card" style="left:34px;top:152px"><div class="icon"></div><div class="lbl">Bruising</div><div class="grid">
    <div class="r"><span># of Claims</span><em>2</em></div><div class="r"><span>Claim Amount</span><em>$7,759</em></div><div class="r"><span>Mod Impact</span><em>0.011</em></div><div class="r last"><span>3 year Premium Cost</span><em>$6,600</em></div></div></div>
  <div class="card" style="left:261px;top:152px"><div class="icon"></div><div class="lbl">Laceration</div><div class="grid" style="left:51px">
    <div class="r"><span># of Claims</span><em>3</em></div><div class="r"><span>Claim Amount</span><em>$73,917</em></div><div class="r"><span>Mod Impact</span><em>0.13</em></div><div class="r last"><span>3 year Premium Cost</span><em>$78,000</em></div></div></div>

  <div class="card" style="left:34px;top:221px"><div class="icon"></div><div class="lbl">Burn or Scald</div><div class="grid">
    <div class="r"><span># of Claims</span><em>2</em></div><div class="r"><span>Claim Amount</span><em>$2,990</em></div><div class="r"><span>Mod Impact</span><em>0.005</em></div><div class="r last"><span>3 year Premium Cost</span><em>$3,000</em></div></div></div>
  <div class="card" style="left:261px;top:221px"><div class="icon"></div><div class="lbl">Poisoning</div><div class="grid" style="left:51px">
    <div class="r"><span># of Claims</span><em>1</em></div><div class="r"><span>Claim Amount</span><em>$7,436</em></div><div class="r"><span>Mod Impact</span><em>0.034</em></div><div class="r last"><span>3 year Premium Cost</span><em>$20,400</em></div></div></div>

  <div class="card" style="left:34px;top:296px"><div class="icon"></div><div class="lbl">Concussion</div><div class="grid">
    <div class="r"><span># of Claims</span><em>2</em></div><div class="r"><span>Claim Amount</span><em>$22,991</em></div><div class="r"><span>Mod Impact</span><em>0.031</em></div><div class="r last"><span>3 year Premium Cost</span><em>$18,600</em></div></div></div>
  <div class="card" style="left:261px;top:296px"><div class="icon"></div><div class="lbl">Sprain or Tear</div><div class="grid" style="left:51px">
    <div class="r"><span># of Claims</span><em>2</em></div><div class="r"><span>Claim Amount</span><em>$5,296</em></div><div class="r"><span>Mod Impact</span><em>0.015</em></div><div class="r last"><span>3 year Premium Cost</span><em>$9,000</em></div></div></div>

  <div class="card" style="left:34px;top:371px"><div class="icon"></div><div class="lbl">Crushing</div><div class="grid">
    <div class="r"><span># of Claims</span><em>2</em></div><div class="r"><span>Claim Amount</span><em>$34,115</em></div><div class="r"><span>Mod Impact</span><em>0.113</em></div><div class="r last"><span>3 year Premium Cost</span><em>$67,800</em></div></div></div>
  <div class="card" style="left:261px;top:371px"><div class="icon"></div><div class="lbl">Strain or Tear</div><div class="grid" style="left:51px">
    <div class="r"><span># of Claims</span><em>5</em></div><div class="r"><span>Claim Amount</span><em>$110,669</em></div><div class="r"><span>Mod Impact</span><em>0.087</em></div><div class="r last"><span>3 year Premium Cost</span><em>$52,200</em></div></div></div>

  <p class="disclaimer">Proprietary and Confidential. Ratewell Inc. provides for an ESTIMATE of an experience modification factor. Your official experience modification factor is issued solely by the applicable workers' compensation rating bureau. Ratewell Inc. All Rights Reserved.</p>
  <div class="brand" style="left:335px;top:592px"><i></i>CLAIMWISE</div>
  <div class="pg">Pg 5</div>
</section>

</body>
</html>
```